Commercial Business Card - stand out, clean, simple, unique.

commercial real estate group located in Texas. Called 4 Ridges Real Estate. We want a unique yet clean and professional card. On one side I would like the 4R to be by itself or to look as unique or tasteful as possible. We have the logo in white, black, and color in case a black background or something similar looks best on one side. We need a space for our name, email, cell. website. And possibly room for a phrase or city.

Contact Information for Business Card

Name, Title, Email, Phone Number, website

```html
<!DOCTYPE html>
<html lang="en">
<head>
<meta charset="utf-8">
<title>4 Ridges Real Estate – Business Card</title>
<link rel="stylesheet" href="https://fonts.googleapis.com/css2?family=Cinzel:wght@600&family=Open+Sans:wght@400;600&display=swap">
<style>
  :root {
    --stage: #e9eaec;
    --card: #ffffff;
    --navy: #1c2f6e;
    --orange: #d0713a;
    --ink: #3d3d3d;
    --muted: #6b6b6b;
    --card-shadow: 0 12px 30px rgba(0,0,0,0.14);
  }
  * { margin: 0; padding: 0; box-sizing: border-box; }
  html, body { width: 1200px; height: 1000px; overflow: hidden; }
  body {
    background: var(--stage);
    font-family: "Open Sans", Arial, sans-serif;
    position: relative;
  }
  .card {
    position: absolute;
    left: 220px;
    width: 760px;
    height: 434px;
    background: var(--card);
    box-shadow: var(--card-shadow);
  }
  .card--back { top: 56px; }
  .card--front { top: 512px; }

  /* Back side */
  .brand-lockup {
    position: absolute;
    top: 150px;
    left: 0; right: 0;
    display: flex;
    align-items: center;
    justify-content: center;
    gap: 18px;
  }
  .brand-mark {
    width: 20px; height: 20px;
    background: var(--navy);
  }
  .brand-name {
    font-family: "Cinzel", Georgia, serif;
    font-weight: 600;
    font-size: 40px;
    letter-spacing: 2px;
    color: var(--navy);
  }
  .tagline {
    position: absolute;
    top: 268px;
    left: 0; right: 0;
    text-align: center;
    font-size: 17px;
    color: var(--muted);
  }

  /* Front side */
  .contact {
    position: absolute;
    left: 60px;
    top: 236px;
    padding-left: 20px;
    border-left: 4px solid var(--navy);
    font-size: 19px;
    line-height: 27px;
    color: var(--ink);
  }
  .holder {
    position: absolute;
    right: 60px;
    top: 54px;
    padding-right: 18px;
    border-right: 4px solid var(--navy);
    text-align: right;
  }
  .holder__name {
    font-weight: 600;
    font-size: 22px;
    letter-spacing: 1px;
    color: var(--navy);
    line-height: 26px;
  }
  .holder__title {
    font-size: 17px;
    letter-spacing: 1px;
    color: var(--orange);
    line-height: 22px;
  }
  .front-brand {
    position: absolute;
    right: 60px;
    bottom: 54px;
    font-family: "Cinzel", Georgia, serif;
    font-weight: 600;
    font-size: 30px;
    letter-spacing: 2px;
    color: var(--navy);
  }
</style>
</head>
<body>
  <section class="card card--back" aria-label="Business card back">
    <div class="brand-lockup">
      <span class="brand-mark"></span>
      <span class="brand-name">4 Ridges Real Estate</span>
    </div>
    <p class="tagline">Find your ideal home</p>
  </section>

  <section class="card card--front" aria-label="Business card front">
    <div class="holder">
      <p class="holder__name">MARA ELLISON</p>
      <p class="holder__title">PRESIDENT</p>
    </div>
    <div class="contact">
      <p>P: 512 604 7719</p>
      <p>M: 512 938 2406</p>
      <p>E: mara@4ridges.com</p>
      <p>W: www.4ridges.com</p>
    </div>
    <p class="front-brand">4 Ridges Real Estate</p>
  </section>
</body>
</html>
```